POOL BUILDING CONTRACTOR

our company has shifter focus over the past 18 month we no longer have a retail store and no longer clean pools we build concrete pools. our website if 5 years old we need a completely new site that shows our core product, building concrete pools & renovate concrete pools

here is a few of our competitors;
brantelwaters.com
okvimbuilders.com
ridgeviewlagoonworks.com
plunvora.com
halvertonbasinsandtubs.com
dremblewaterne.com

one we land on a final design I will upload customer before and after photos and any other content needed

Target Market(s)

People looking to build or renovate there pool

Industry/Entity Type

swimming pool

Coding

Coded - Design and coding required

Number of Pages Required

5+ page

Colors
0054AA
0677BA
7BADD7
CADEEF
E8F1F8

Requirements
Must have
• financing Service-Repairs & liners new build-photos renovate-remodeling design-consult customer-reviews Gallery Before-After Contact us 3D Design & Modeling construction process & Timeline Equipment Features Hardscapes I like these sites https://meadowlarkbasinsbycraft.com/ https://holtbergwaters.com/

```html
<!DOCTYPE html>
<html lang="en">
<head>
<meta charset="utf-8">
<title>Tidewell – Concrete Pool Building and Renovation</title>
<link href="https://fonts.googleapis.com/css2?family=Righteous&family=Poppins:wght@400;500;600&display=swap" rel="stylesheet">
<style>
:root{
  --slate:#4a6389;
  --cyan:#19b6ea;
  --text:#3c4656;
  --band:#f1f1f2;
  --white:#ffffff;
}
*{box-sizing:border-box;margin:0;padding:0}
html,body{width:1200px;height:3803px;overflow:hidden}
body{position:relative;background:var(--white);font-family:"Poppins",sans-serif;color:var(--text)}
.abs{position:absolute}
.display{font-family:"Righteous",sans-serif;font-weight:400;color:var(--slate)}
.photo{position:absolute;border-radius:50%}
.btn{position:absolute;display:flex;align-items:center;justify-content:center;border-radius:22px;font-size:12px;font-weight:600;white-space:nowrap}
.btn-cyan{background:var(--cyan);color:var(--white)}
.btn-white{background:var(--white);color:var(--slate)}
.btn-ghost{border:1.5px solid var(--white);color:var(--white)}
.brand{position:absolute;display:flex;align-items:center;gap:8px;color:var(--white)}
.brand-mark{width:44px;height:44px;border:2px solid var(--white)}
.brand-name{font-family:"Poppins",sans-serif;font-weight:600;font-size:30px;line-height:1}
.brand-tag{font-size:7.5px;font-weight:600;letter-spacing:.3px;color:var(--white)}
.nav{position:absolute;display:flex;gap:31px;font-size:14px}
.nav a{color:inherit;text-decoration:none}

.hero{position:absolute;left:0;top:0;width:1200px;height:620px;
  background:linear-gradient(180deg,#6d8f96 0%,#2f7f93 28%,#1c6e86 55%,#14617a 100%)}
.hero-title{position:absolute;left:0;width:1200px;text-align:center;font-family:"Righteous",sans-serif;font-weight:400;color:var(--white);font-size:52px;line-height:59px;top:200px}
.hero-sub{position:absolute;left:0;width:1200px;text-align:center;color:var(--white);font-size:15px;top:324px}

.tag{font-family:"Righteous",sans-serif;color:var(--cyan);font-size:15px}
.copy{font-size:12.6px;line-height:18px;color:var(--text)}
.center{text-align:center}

.cat-photo{width:222px;height:222px;top:1274px}
.cat-badge{position:absolute;width:102px;height:102px;border-radius:50%;background:var(--slate);top:1425px;display:flex;align-items:center;justify-content:center}
.cat-label{position:absolute;top:1556px;width:260px;text-align:center;font-size:32px}

.bullets{list-style:none;font-size:12.6px;line-height:21.6px}
.bullets li{padding-left:18px;position:relative}
.bullets li::before{content:"";position:absolute;left:2px;top:9px;width:5px;height:5px;border-radius:50%;background:var(--text)}

.gal{width:222px;height:222px;top:2661px}
.dot{position:absolute;width:5px;height:5px;border-radius:50%;background:var(--slate);top:2938px}

.pill{position:absolute;background:var(--slate);color:var(--white);font-family:"Righteous",sans-serif;font-size:15px;border-radius:18px;display:flex;align-items:center;justify-content:center}
.arrow{position:absolute;width:31px;height:31px;border-radius:50%;background:var(--cyan);top:3367px}

.footer-nav{position:absolute;top:3661px;left:378px;display:flex;gap:29px;font-size:12.6px;color:var(--white)}
.social{position:absolute;top:3693px;width:30px;height:30px;border-radius:50%;background:var(--white)}
</style>
</head>
<body>

<!-- HERO -->
<section class="hero" role="img" aria-label="Resort swimming pool with palm trees and thatched sun umbrellas by the sea"></section>
<svg class="abs" style="left:0;top:440px" width="1200" height="200" viewBox="0 0 1200 200" aria-hidden="true">
  <path d="M0 125 C40 110 50 40 100 45 C150 50 150 95 200 95 C260 95 330 40 420 40 C500 40 520 100 560 140 C600 180 560 80 640 75 C720 70 760 120 860 105 C950 90 980 50 1060 45 C1120 42 1160 60 1200 70 L1200 200 L0 200 Z" fill="#ffffff"/>
  <ellipse cx="110" cy="110" rx="35" ry="18" fill="#ffffff" transform="rotate(25 110 110)"/>
</svg>

<div class="brand" style="left:80px;top:27px">
  <div class="brand-mark"></div>
  <div>
    <div class="brand-name">Tidewell</div>
    <div class="brand-tag">CONCRETE POOL BUILDERS</div>
  </div>
</div>
<nav class="nav" style="left:384px;top:39px;color:var(--white)">
  <a>About Us</a><a>New Builds</a><a>Renovation</a><a>Gallery</a><a>Financing</a>
</nav>
<div class="btn btn-ghost" style="left:954px;top:31px;width:149px;height:38px">Request a Quote</div>

<h1 class="hero-title">Dreaming Of A New Pool ?<br>We Build It In Concrete</h1>
<p class="hero-sub">custom design, 3D modeling and financing for every build</p>
<div class="btn btn-white" style="left:525px;top:366px;width:150px;height:37px">Explore More</div>

<!-- ABOUT -->
<p class="tag abs" style="left:148px;top:686px">About Tidewell</p>
<h2 class="display abs" style="left:148px;top:708px;font-size:31px;line-height:40px;width:470px">Concrete Pool Building and Renovation Company</h2>
<p class="copy abs" style="left:148px;top:800px;width:448px">Tidewell designs and builds custom concrete pools for homeowners who want a backyard that lasts. From the first consult and 3D design to excavation, steel, plumbing, shotcrete, tile and coping, our own crews handle every step. We also renovate and remodel tired concrete pools with new plaster, tile, equipment and hardscapes, and offer repairs and liners, with financing options to fit your budget.</p>
<div class="btn btn-cyan" style="left:145px;top:941px;width:129px;height:36px">Explore More</div>
<div class="photo" style="left:634px;top:638px;width:400px;height:400px;background:linear-gradient(180deg,#5aa6d8 0%,#9cc8e6 30%,#2f8fc4 55%,#1a5fa8 100%)" role="img" aria-label="Finished concrete pool edge with a lounge chair and float on the water"></div>

<!-- SERVICES -->
<h2 class="display abs center" style="left:0;width:1180px;top:1133px;font-size:34px">What We Build</h2>
<p class="copy abs center" style="left:250px;width:680px;top:1184px">Every project is designed around your yard and built in concrete by our own crews, from the first sketch to the final fill, with clear pricing and a set timeline.</p>

<div class="photo cat-photo" style="left:78px;background:linear-gradient(135deg,#e8b860,#5aa3c9 55%,#2c6fa0)" role="img" aria-label="Newly built concrete pool in a backyard"></div>
<div class="photo cat-photo" style="left:346px;background:linear-gradient(135deg,#b7c8d6,#3a87b8 55%,#1d5a86)" role="img" aria-label="Pool being replastered during a renovation"></div>
<div class="photo cat-photo" style="left:612px;background:linear-gradient(135deg,#dce6ee,#5b98c9 55%,#2864a5)" role="img" aria-label="3D design rendering of a pool layout"></div>
<div class="photo cat-photo" style="left:881px;background:linear-gradient(135deg,#c9b9a4,#5ba7d8 55%,#1b5a9a)" role="img" aria-label="Stone pool deck and hardscape around a pool"></div>

<div class="cat-badge" style="left:92px"><svg width="46" height="46" viewBox="0 0 46 46" fill="none" stroke="#fff" stroke-width="2" stroke-linejoin="round"><path d="M7 22 23 9l16 13M11 19v17h24V19"/><path d="M19 36v-9h8v9"/></svg></div>
<div class="cat-badge" style="left:362px"><svg width="46" height="46" viewBox="0 0 46 46" fill="none" stroke="#fff" stroke-width="2" stroke-linecap="round"><path d="M10 36 28 18M26 10a8 8 0 0 0 10 10l-4-4-2-2z"/></svg></div>
<div class="cat-badge" style="left:631px"><svg width="46" height="46" viewBox="0 0 46 46" fill="none" stroke="#fff" stroke-width="2" stroke-linejoin="round"><path d="M23 8 37 15v16l-14 7-14-7V15z"/><path d="M9 15l14 7 14-7M23 22v16"/></svg></div>
<div class="cat-badge" style="left:901px"><svg width="46" height="46" viewBox="0 0 46 46" fill="none" stroke="#fff" stroke-width="2"><rect x="8" y="11" width="30" height="24"/><path d="M8 19h30M8 27h30M18 11v8M28 19v8M18 27v8"/></svg></div>

<div class="cat-label display" style="left:54px">New Builds</div>
<div class="cat-label display" style="left:325px">Renovation</div>
<div class="cat-label display" style="left:595px">3D Design</div>
<div class="cat-label display" style="left:865px">Hardscapes</div>

<div class="btn btn-cyan" style="left:530px;top:1651px;width:122px;height:38px">View All</div>

<!-- GREY BAND -->
<svg class="abs" style="left:0;top:2320px" width="1200" height="720" viewBox="0 0 1200 720" aria-hidden="true">
  <path d="M0 60 C200 140 500 140 750 80 C950 30 1100 20 1200 18 L1200 620 C1050 660 850 720 600 690 C350 660 150 600 0 600 Z" fill="#f1f1f2"/>
</svg>

<!-- PROCESS -->
<div class="photo" style="left:-130px;top:1753px;width:660px;height:660px;background:linear-gradient(180deg,#2f6fb4 0%,#8fc0e6 35%,#e6f1f8 52%,#2b88c9 62%,#4aaee3 80%,#1f5fa6 100%)" role="img" aria-label="Concrete infinity pool with steel ladder overlooking the ocean"></div>

<p class="tag abs" style="left:586px;top:1836px;font-size:13px">CONSTRUCTION PROCESS</p>
<h2 class="display abs" style="left:586px;top:1857px;font-size:31px;line-height:40px">From Consult To First Swim<br>In About 12 Weeks</h2>
<div class="copy abs" style="left:586px;top:1947px;width:455px">
  <p>Whether you want a brand new pool or a full remodel, Tidewell's build team guides you through every stage so you always know what comes next.</p>
  <p style="margin-top:4px">We are committed to building concrete pools that stand up to the years, with engineered steel, quality shotcrete and careful finish work.</p>
  <p style="margin-top:6px">Every build follows the same clear timeline from start to finish.</p>
</div>
<ul class="bullets abs" style="left:586px;top:2097px">
  <li>Design consult and site visit</li>
  <li>3D design and modeling of your pool</li>
  <li>Permits, layout and excavation</li>
  <li>Steel, plumbing and electrical rough-in</li>
  <li>Shotcrete shell and curing</li>
  <li>Tile, coping, equipment and hardscapes</li>
  <li>Interior finish, fill and start-up</li>
</ul>
<p class="copy abs" style="left:586px;top:2263px;width:455px">Flexible financing is available on new builds and renovations, so you can start your project now and pay over time with a plan that suits you.</p>
<div class="btn btn-cyan" style="left:586px;top:2340px;width:199px;height:37px">Call today 555-014-2290.</div>

<!-- GALLERY -->
<h2 class="display abs center" style="left:0;width:1180px;top:2523px;font-size:34px">Our Gallery</h2>
<p class="copy abs center" style="left:250px;width:680px;top:2574px">A look at concrete pools we have designed and built, from compact plunge pools to resort style backyards with spas, water features and full hardscapes.</p>

<div class="photo gal" style="left:115px;background:linear-gradient(180deg,#e7ecef,#8fa98a 45%,#2b8fc0 80%)" role="img" aria-label="Modern villa pool with umbrellas and palm trees"></div>
<div class="photo gal" style="left:364px;background:linear-gradient(180deg,#3f86cf,#8dc3e8 45%,#4ec6e4 70%,#6b6f74)" role="img" aria-label="Infinity pool overlooking a tropical bay"></div>
<div class="photo gal" style="left:612px;background:linear-gradient(180deg,#9bb9c8,#3d5a4c 40%,#2d8a9f 65%,#1e5e73)" role="img" aria-label="Pavilion beside a long pool among trees"></div>
<div class="photo gal" style="left:863px;background:linear-gradient(180deg,#e8eef1,#d67d6d 35%,#26b7d6 65%,#1796bd)" role="img" aria-label="Large pool with ladders and colourful buildings"></div>

<div class="dot" style="left:534px"></div>
<div class="dot" style="left:570px"></div>
<div class="abs" style="left:593px;top:2925px;width:31px;height:31px;border-radius:50%;border:1.5px solid var(--slate)"></div>
<div class="dot" style="left:606px"></div>
<div class="dot" style="left:643px"></div>

<!-- RENOVATION -->
<p class="tag abs" style="left:158px;top:3188px">Before &amp; After</p>
<h2 class="display abs" style="left:158px;top:3208px;font-size:31px">Renovation &amp; Restoration</h2>
<p class="copy abs" style="left:158px;top:3262px;width:390px">We bring worn concrete pools back to life with new plaster, tile, coping, equipment and decking. See how our remodels turn a tired backyard pool into a space your family will enjoy again for years to come.</p>
<div class="arrow" style="left:157px"><svg width="31" height="31" viewBox="0 0 31 31"><path d="M21 15.5H10M14 11l-4.5 4.5L14 20" fill="none" stroke="#fff" stroke-width="1.8" stroke-linecap="round" stroke-linejoin="round"/></svg></div>
<div class="arrow" style="left:196px"><svg width="31" height="31" viewBox="0 0 31 31"><path d="M10 15.5h11M17 11l4.5 4.5L17 20" fill="none" stroke="#fff" stroke-width="1.8" stroke-linecap="round" stroke-linejoin="round"/></svg></div>

<div class="photo" style="left:618px;top:3139px;width:395px;height:395px;background:linear-gradient(180deg,#6f7a6a 0%,#3f7fa9 35%,#1f6aa8 60%,#b9b4aa 100%)" role="img" aria-label="Renovated backyard pool after restoration"></div>
<div class="photo" style="left:827px;top:3055px;width:236px;height:236px;border:4px solid var(--white);background:linear-gradient(180deg,#c8d2d6 0%,#5a7754 35%,#4db9dc 60%,#c7a898 100%)" role="img" aria-label="Backyard pool before restoration"></div>
<div class="pill" style="left:795px;top:3110px;width:89px;height:33px">Before</div>
<div class="pill" style="left:595px;top:3396px;width:89px;height:33px">After</div>

<!-- FOOTER -->
<svg class="abs" style="left:0;top:3480px" width="1200" height="323" viewBox="0 0 1200 323" aria-hidden="true">
  <path d="M0 75 C60 55 130 45 190 50 C240 55 260 80 330 70 C420 58 480 30 560 45 C640 60 640 95 720 100 C820 106 900 70 980 60 C1050 52 1080 85 1130 40 C1160 15 1185 10 1200 12 L1200 323 L0 323 Z" fill="#4a6389"/>
</svg>

<div class="brand" style="left:80px;top:3617px">
  <div class="brand-mark" style="width:52px;height:52px"></div>
  <div>
    <div class="brand-name" style="font-size:36px">Tidewell</div>
    <div class="brand-tag" style="font-size:8.5px">CONCRETE POOL BUILDERS</div>
  </div>
</div>
<div class="social" style="left:80px"></div>
<div class="social" style="left:122px"></div>
<div class="social" style="left:164px"></div>

<nav class="footer-nav">
  <span>About Us</span><span>New Builds</span><span>Renovation</span><span>Gallery</span><span>Financing</span>
</nav>

<h2 class="abs" style="left:842px;top:3613px;font-family:'Righteous',sans-serif;font-weight:400;font-size:32px;color:var(--white)">Get In Touch</h2>
<div class="abs" style="left:829px;top:3661px;width:275px;height:48px;border:1.5px solid var(--white);border-radius:24px"></div>
<p class="abs" style="left:848px;top:3677px;font-size:12.6px;color:var(--white)">Enter your email</p>
<div class="btn btn-white" style="left:1003px;top:3661px;width:101px;height:48px;border-radius:24px;font-size:15px;font-weight:500">Submit</div>

<div class="abs" style="left:0;top:3757px;width:1200px;height:1px;background:rgba(255,255,255,.6)"></div>
<p class="abs center" style="left:0;width:1180px;top:3771px;font-size:13px;color:var(--white)">© 2023 <strong>Tidewell</strong>. All Rights Reserved</p>

</body>
</html>
```